Olive oil bottle labels, front and back.

Sophisticated uncluttered distinctive eye catching label
Front label:
Label on front like the uploaded file in design but called “Corrowick Hollow”, (not Marrabel Reach.)
Need to state that it’s extra virgin, cold pressed olive oil, 100% organic, grown and pressed on the Mornington Peninsula.
500 ml
Back label:
Nutritional information table (see label example in uploaded files) including FFA 0.1% Oleic Acid
Storage: airtight in cool dark place
Made and produced in Australia from 100% Australian ingredients,
Harvest date:
Best by:
Batch:
Grown, harvested and bottled at The Hollow, Pellandry Rd. Flinders. 3847
The back label on uploaded files has the info requited except they should have address and don't include those industry and Australian made logos.
The front label is what we want, first to plagiarise without copyright infringement gets the gig, thanks.
Labels front and back need be 5 x 13 cm
Gourmet, up-market
- Love "Adorn Regular Garland"

```html
<!DOCTYPE html>
<html lang="en">
<head>
<meta charset="utf-8">
<title>Corrowick Hollow Extra Virgin Olive Oil – Front and Back Labels</title>
<link rel="stylesheet" href="https://fonts.googleapis.com/css2?family=Pinyon+Script&family=Tinos:wght@400;700&family=Arimo:wght@400;700&display=swap">
<style>
  :root {
    --page: #ffffff;
    --label-dark: #161616;
    --label-mid: #2a2a2a;
    --gold: #d49a1c;
    --gold-soft: #b98a2e;
    --ink-light: #f2f2f2;
    --ink-grey: #cfcfcf;
    --rule: #d8d8d8;
  }
  * { box-sizing: border-box; margin: 0; padding: 0; }
  html, body { width: 1200px; height: 1200px; overflow: hidden; background: var(--page); }
  .canvas { position: relative; width: 1200px; height: 1200px; background: var(--page); }

  .label {
    position: absolute;
    overflow: hidden;
    background:
      radial-gradient(ellipse at 70% 60%, rgba(255,255,255,0.07), transparent 60%),
      linear-gradient(90deg, var(--label-dark), var(--label-mid) 55%, var(--label-dark));
    box-shadow: 6px 8px 10px rgba(0,0,0,0.35);
  }
  .label--front { left: 195px; top: 113px; width: 383px; height: 990px; }
  .label--back  { left: 635px; top: 113px; width: 393px; height: 1005px; }

  /* artwork areas */
  .silk-waves {
    position: absolute; inset: 0;
    background: linear-gradient(100deg, transparent 40%, rgba(255,255,255,0.06) 60%, transparent 80%);
  }
  .oil-artwork {
    position: absolute; left: 40px; top: 0; width: 310px; height: 640px;
    background: radial-gradient(ellipse 50% 50% at 50% 55%, rgba(214,148,28,0.85), rgba(170,108,14,0.45) 55%, transparent 100%);
  }
  .back-artwork {
    position: absolute; left: 90px; top: 0; width: 220px; height: 360px;
    background: radial-gradient(ellipse 50% 60% at 50% 20%, rgba(190,130,25,0.45), transparent 100%);
  }

  .halo {
    position: absolute; left: -5px; top: 290px; width: 384px; height: 384px;
    border: 2px solid var(--gold-soft); border-radius: 50%;
  }

  .brand-name {
    position: absolute; left: 185px; top: 570px;
    width: 700px; margin-left: -350px; margin-top: -45px;
    transform: rotate(-84deg);
    font-family: "Pinyon Script", cursive; font-weight: 400;
    font-size: 74px; line-height: 90px; color: var(--ink-light);
    white-space: nowrap; text-align: center;
  }

  .product-type {
    position: absolute; left: 210px; top: 720px;
    font-family: "Tinos", serif; color: var(--ink-grey);
    font-size: 24px; line-height: 27px; letter-spacing: 0.5px;
  }
  .product-type .olive { color: var(--gold); }
  .product-type .volume { font-size: 15px; margin-top: 14px; }

  .certification {
    position: absolute; left: 0; top: 875px; width: 200px;
    text-align: center; font-family: "Tinos", serif; color: var(--ink-light);
  }
  .certification .percent { font-size: 20px; }
  .certification .organic {
    display: inline-block; font-size: 21px; font-weight: 700; letter-spacing: 1px;
    border-top: 1px solid var(--gold-soft); border-bottom: 1px solid var(--gold-soft);
    padding: 1px 4px;
  }
  .certification .note { font-size: 8px; line-height: 10px; margin: 6px auto 0; width: 170px; }

  /* back */
  .variety { position: absolute; left: 0; right: 0; top: 100px; text-align: center;
    font-family: "Arimo", sans-serif; font-weight: 700; color: var(--ink-light); }
  .variety .kicker { font-size: 20px; }
  .variety .cultivar { font-size: 44px; line-height: 50px; margin-left: -20px; }
  .variety .style { font-size: 20px; margin-left: -20px; }

  .nutrition {
    position: absolute; left: 45px; top: 289px; width: 268px;
    border: 1px solid var(--rule); padding: 6px 6px 8px;
    font-family: "Arimo", sans-serif; color: var(--ink-light);
  }
  .nutrition h2 { font-size: 18px; font-weight: 400; padding-left: 4px; }
  .nutrition table { width: 100%; border-collapse: collapse; font-size: 12px; }
  .nutrition th { font-weight: 400; font-size: 8px; text-align: left; line-height: 9px; vertical-align: bottom; padding-bottom: 4px; }
  .nutrition th.avg { font-size: 15px; padding-left: 8px; }
  .nutrition td { height: 20px; border-bottom: 1px solid var(--rule); padding: 0 2px; }
  .nutrition td:first-child { font-weight: 700; font-size: 11px; }
  .nutrition td.num { width: 46px; font-size: 13px; border-left: 1px solid var(--rule); }
  .nutrition tr.spacer td { border-bottom: none; height: 20px; }
  .nutrition .storage-note { font-size: 10px; padding-top: 7px; }

  .batch-info, .provenance {
    position: absolute; left: 43px; font-family: "Arimo", sans-serif;
    color: var(--ink-light); font-size: 14.5px; line-height: 20px;
  }
  .batch-info { top: 722px; }
  .provenance { top: 812px; width: 330px; }
  .origin { position: absolute; left: 45px; top: 895px;
    font-family: "Arimo", sans-serif; color: var(--ink-light); font-size: 14.5px; line-height: 23px; }
  .origin .first { padding-left: 25px; }
</style>
</head>
<body>
<main class="canvas">
  <section class="label label--front" aria-label="Front label">
    <div class="silk-waves" role="img" aria-label="Fine flowing white line waves across the dark background"></div>
    <div class="oil-artwork" role="img" aria-label="Illustration of golden olive oil pouring into a glowing drop"></div>
    <div class="halo"></div>
    <h1 class="brand-name">Corrowick Hollow</h1>
    <div class="product-type">
      <div>EXTRA</div>
      <div>VIRGIN</div>
      <div class="olive">OLIVE OIL</div>
      <div class="volume">500ML</div>
    </div>
    <div class="certification">
      <div class="percent">100%</div>
      <div class="organic">ORGANIC</div>
      <p class="note">EXTRA VIRGIN, COLD PRESSED OLIVE OIL. GROWN AND PRESSED ON THE MORNINGTON PENINSULA.</p>
    </div>
  </section>

  <section class="label label--back" aria-label="Back label">
    <div class="silk-waves" role="img" aria-label="Fine flowing white line waves across the dark background"></div>
    <div class="back-artwork" role="img" aria-label="Faint golden olive oil stream illustration"></div>
    <div class="variety">
      <div class="kicker">variety</div>
      <div class="cultivar">CORA+ INA</div>
      <div class="style">(Denocciolate)</div>
    </div>
    <div class="nutrition">
      <h2>NUTRITION INFORMATION</h2>
      <table>
        <tr><th class="avg">AVG OTY</th><th>PER<br>15ML</th><th>PER<br>100ML</th></tr>
        <tr><td>ENERGY (KJ)</td><td class="num">517</td><td class="num">3446</td></tr>
        <tr><td>PROTEIN</td><td class="num">517</td><td class="num">517</td></tr>
        <tr><td>FAT (G)</td><td class="num">517</td><td class="num">517</td></tr>
        <tr class="spacer"><td></td><td class="num"></td><td class="num"></td></tr>
        <tr><td>TOTAL</td><td class="num">13.7</td><td class="num">91.5</td></tr>
        <tr><td>SATURED</td><td class="num">2.1</td><td class="num">14.1</td></tr>
        <tr><td>MONOUNSATURATED</td><td class="num">10.7</td><td class="num">71.5</td></tr>
        <tr><td>POLYUNSATURATED</td><td class="num">0.9</td><td class="num">5.9</td></tr>
        <tr><td>TRANS FATTY ACID</td><td class="num">&lt;0.01</td><td class="num">&lt;0.05</td></tr>
        <tr><td>CHOLESTEROL(MG)</td><td class="num">0</td><td class="num">0</td></tr>
        <tr><td>CARBOIDRATE (G)</td><td class="num">0</td><td class="num">0</td></tr>
        <tr><td>SUGAR (G)</td><td class="num">0</td><td class="num">0</td></tr>
        <tr><td>FFA (OLEIC ACID)</td><td class="num">0.1%</td><td class="num">0.1%</td></tr>
      </table>
      <p class="storage-note">STORE AIRTIGHT IN A DARK, COOL PLACE</p>
    </div>
    <div class="batch-info">
      <div>Harvest date:</div>
      <div>Best by:</div>
      <div>Batch:</div>
    </div>
    <div class="provenance">
      <div>Storage: airtight in cool dark place</div>
      <div>Made and produced in Australia from 100%</div>
      <div>Australian ingredients,</div>
    </div>
    <div class="origin">
      <div class="first">Grown, harvested and bottled</div>
      <div>at The Hollow, Pellandry Rd. Flinders. 3847</div>
      <div>Hollow, Pellandry Rd. Flinders. 3847</div>
    </div>
  </section>
</main>
</body>
</html>
```